Coralinks.com website overhaul

We want to upgrade our Wix website into a professional looking page for our growing business. The content that is online now needs to be used but the site should have a new look and feel from top to bottom. CoraLinks is a company in the hospital and nursing home space. We would like to see the website use our color scheme but other than that we are open to any and all ideas. www.coralinks.com

```html
<!DOCTYPE html>
<html lang="en">
<head>
<meta charset="utf-8">
<title>CoraLinks – Air Filtration System</title>
<link href="https://fonts.googleapis.com/css2?family=Montserrat:wght@500;600;700&family=Roboto:wght@400;500&display=swap" rel="stylesheet">
<style>
:root{
  --brand:#4a4fa6;
  --brand-dark:#2c1a5a;
  --ink:#1c1b2e;
  --body:#333340;
  --nav-active:#6a4fd6;
  --tint:#f3f3fa;
  --line:#9a9aa6;
}
*{margin:0;padding:0;box-sizing:border-box}
html,body{width:1200px;height:4500px;overflow:hidden;background:#fff}
body{position:relative;font-family:"Roboto",Arial,sans-serif;color:var(--body)}
.abs{position:absolute}
h1,h2,h3,.logo,.btn{font-family:"Montserrat",Arial,sans-serif}
.logo{display:flex;align-items:center;gap:14px;color:#3a1f6b;font-weight:600;font-size:44px}
.logo .mark{width:40px;height:40px;background:var(--brand)}
.topbar{left:716px;top:0;width:484px;height:35px;background:var(--brand-dark);color:#fff;font-size:15px;display:flex;align-items:center;justify-content:flex-end;gap:26px;padding-right:100px}
.nav{top:58px;right:98px;display:flex;gap:48px;font-family:"Montserrat",sans-serif;font-weight:600;font-size:17px;color:var(--ink)}
.nav .active{color:var(--nav-active)}
.hero{left:0;top:117px;width:1200px;height:526px;background:linear-gradient(180deg,#4a4a4e,#2e2e32)}
.hero-title{left:101px;top:262px;color:#fff;font-size:58px;font-weight:700;line-height:68px}
.btn{display:flex;align-items:center;justify-content:center;background:var(--brand);color:#fff;font-weight:600;font-size:17px}
.slides{left:100px;top:586px;display:flex;gap:12px}
.slides span{width:40px;height:2px;background:#fff}
.slides span:first-child{background:var(--brand)}
.media{display:block}
.section-title{width:1200px;left:0;text-align:center;font-weight:600;color:var(--ink);font-size:40px}
.text{font-size:14.5px;line-height:29px}
.card{border:2px solid var(--brand);background:var(--tint);padding:0 26px;display:flex;flex-direction:column;justify-content:center}
.card h3{font-size:31px;font-weight:600;color:var(--ink);line-height:38px;margin-bottom:10px}
.card p{font-size:14.5px;line-height:26px}
.card .more{margin-top:14px;color:var(--brand);font-weight:600;font-size:16px;font-family:"Montserrat",sans-serif}
.field{font-size:15px;color:var(--ink);border-bottom:1.5px solid var(--line);padding-bottom:6px}
.band{left:0;top:3894px;width:1200px;height:257px;background:var(--brand-dark)}
.foot-h{font-family:"Montserrat",sans-serif;font-weight:600;font-size:18px;color:var(--ink)}
.foot-l{font-size:15px;color:var(--ink)}
</style>
</head>
<body>

<header>
  <div class="abs topbar"><span>✉ hello@coralinks.com</span><span>☎ 555-014-2290</span></div>
  <div class="abs logo" style="left:98px;top:32px"><span class="mark"></span>CoraLinks</div>
  <nav class="abs nav"><span class="active">Home</span><span>How it Works</span><span>Resources</span><span>Contact</span></nav>
</header>

<section>
  <div class="abs hero" role="img" aria-label="Photo of an empty hospital corridor with waiting chairs"></div>
  <svg class="abs" style="left:620px;top:117px" width="520" height="526" role="img" aria-label="Decorative chevron of soft violet dots">
    <defs><linearGradient id="chev" x1="0" x2="1"><stop offset="0" stop-color="#6f74d0" stop-opacity=".55"/><stop offset="1" stop-color="#9fa4ef" stop-opacity=".85"/></linearGradient></defs>
    <polygon points="265,0 523,268 265,526 20,526 20,0" fill="url(#chev)" opacity=".7"/>
  </svg>
  <h1 class="abs hero-title">CoraLinks is<br>an air Filtration<br>System</h1>
  <div class="abs btn" style="left:100px;top:486px;width:166px;height:45px">Contact Us →</div>
  <div class="abs slides"><span></span><span></span><span></span></div>
</section>

<section>
  <div class="abs media" style="left:96px;top:756px;width:481px;height:366px;background:linear-gradient(180deg,#c9d3dc 0%,#b7c3ce 78%,#b7876a 78%,#a8785c 100%)" role="img" aria-label="Illustration of a hospital room with a bed, IV stand and cabinet"></div>
  <svg class="abs" style="left:293px;top:895px" width="88" height="88" aria-hidden="true"><circle cx="44" cy="44" r="40" fill="none" stroke="#fff" stroke-width="5"/><polygon points="34,26 64,44 34,62" fill="#fff"/></svg>
  <h2 class="abs" style="left:614px;top:742px;width:500px;font-size:41px;line-height:48px;font-weight:600;color:var(--ink)">Enhanced Protection Against Airborne Infectious Particles</h2>
  <p class="abs text" style="left:614px;top:898px;width:490px">The CoraLinks board is an air filtration system that reduces the exposure to airborne infectious particles for healthcare workers, patients, and visitors by utilizing a source-focused technology that captures airborne infectious particles at the source. The board utilizes a patent-pending headboard design that pulls air from the head area of the patient through a HEPA filtration system and exhausts filtered air back into the room.</p>
</section>

<section>
  <h2 class="abs section-title" style="top:1268px">How a CoraLinks Works</h2>
  <svg class="abs" style="left:0;top:1345px" width="1200" height="524" viewBox="0 770 687 300" font-family="Roboto, Arial, sans-serif">
    <g fill="none" stroke="#2a2a2a" stroke-width="1">
      <path d="M88,789 H232 V851 H88 A31,31 0 0 1 88,789 Z"/>
      <path d="M90,882 H190 V966 H90 A33,42 0 0 1 90,882 Z"/>
      <path d="M88,994 H232 V1058 H88 A32,32 0 0 1 88,994 Z"/>
      <path d="M455,787 H598 A32,32 0 0 1 598,851 H455 Z"/>
      <path d="M497,882 H596 A33,42 0 0 1 596,966 H497 Z"/>
      <path d="M455,994 H598 A31,31 0 0 1 598,1056 H455 Z"/>
    </g>
    <circle cx="343" cy="922" r="89" fill="none" stroke="#2a2a2a" stroke-width="1.2"/>
    <g fill="#2a2a2a"><circle cx="287" cy="853" r="6"/><circle cx="255" cy="922" r="6"/><circle cx="287" cy="990" r="6"/><circle cx="400" cy="853" r="6"/><circle cx="432" cy="922" r="6"/><circle cx="400" cy="990" r="6"/></g>
    <circle cx="343" cy="922" r="76" fill="#4a4fa6"/>
    <circle cx="343" cy="922" r="64" fill="#f2f2f4"/>
    <rect x="289" y="916" width="11" height="11" fill="#4a4fa6"/>
    <text x="306" y="927" font-family="Montserrat, sans-serif" font-weight="600" font-size="13" fill="#3a1f6b">CoraLinks</text>
    <g fill="#4a4fa6">
      <circle cx="247" cy="822" r="29"/><circle cx="204" cy="922" r="29"/><circle cx="247" cy="1024" r="29"/>
      <circle cx="438" cy="822" r="29"/><circle cx="481" cy="922" r="29"/><circle cx="438" cy="1024" r="29"/>
    </g>
    <g fill="#f4f4f8">
      <circle cx="251" cy="822" r="23"/><circle cx="208" cy="922" r="23"/><circle cx="251" cy="1024" r="23"/>
      <circle cx="434" cy="822" r="23"/><circle cx="477" cy="922" r="23"/><circle cx="434" cy="1024" r="23"/>
    </g>
    <g font-family="Montserrat, sans-serif" font-weight="700" font-size="22" fill="#4a4fa6" text-anchor="middle">
      <text x="249" y="830">01</text><text x="205" y="930">02</text><text x="248" y="1032">03</text>
      <text x="437" y="830">04</text><text x="480" y="930">05</text><text x="438" y="1032">06</text>
    </g>
    <g font-size="8.7" fill="#2a2a2a">
      <text x="77" y="816">A resident shows possible</text><text x="77" y="829">symptoms of an illness or virus.</text>
      <text x="70" y="898">Install CoraLinks System</text><text x="70" y="910">to patient bed and turn</text><text x="70" y="922">on HEPA box on to</text><text x="70" y="934">protect other residents,</text><text x="70" y="946">healthcare workers, and</text><text x="86" y="958">visitors from..</text>
      <text x="75" y="1004">The CoraLinks uses negative</text><text x="75" y="1016">air pressure to help with aerosol</text><text x="75" y="1028">containment before</text><text x="75" y="1040">contaminants have a chance to</text><text x="75" y="1052">disperse.</text>
      <text x="480" y="798">The HEPA filtration reduces the</text><text x="480" y="810">number of airborne infectious</text><text x="480" y="822">particles helping protect the air</text><text x="480" y="834">and surrounding surfaces from</text><text x="480" y="846">contamination.</text>
      <text x="520" y="895">The canopy allows</text><text x="520" y="907">low-velocity air currents</text><text x="520" y="919">to capture and remove</text><text x="520" y="931">airborne infectious</text><text x="520" y="943">particles without</text><text x="520" y="956">irritating the patient.</text>
      <text x="480" y="1010">A typical 20 x 15 patient room</text><text x="480" y="1022">will have the air completely</text><text x="480" y="1034">turned over and cleaned</text><text x="480" y="1047">approximately every 9 minutes.</text>
    </g>
  </svg>
</section>

<section>
  <div class="abs" style="left:0;top:1957px;width:1200px;height:1354px;background:var(--tint)"></div>
  <h2 class="abs section-title" style="top:2040px">Source-Focused HEPA Filtration</h2>
  <p class="abs" style="left:0;top:2103px;width:1200px;text-align:center;font-size:16px;color:var(--ink)">Capture airborne infectious particles at the source</p>

  <div class="abs media" style="left:100px;top:2172px;width:464px;height:279px;background:linear-gradient(180deg,#2b9fc4,#2590b5)" role="img" aria-label="Illustration of a nurse with a clipboard beside a patient in bed"></div>
  <div class="abs card" style="left:585px;top:2201px;width:514px;height:280px">
    <h3>Greater Protection than an N95 Mask*</h3>
    <p>According to the NHA Study, "Expedient Methods for Surge Airborne Isolation within Healthcare Settings during Response to a Natural or Manmade Epidemic", the expedient airborne isolation research discussed within this document has identified</p>
    <span class="more">Read More →</span>
  </div>

  <div class="abs card" style="left:100px;top:2556px;width:513px;height:278px">
    <h3>Deploys in Minutes</h3>
    <p>The CoraLinks board is a complete system that can be deployed in a matter of minutes using only basic tools. The system easily disassembles for sanitation.</p>
  </div>
  <div class="abs media" style="left:636px;top:2524px;width:463px;height:280px;background:linear-gradient(180deg,#b4c4d2,#a6b7c6)" role="img" aria-label="Illustration of a HEPA filter unit drawing air above a bed headboard"></div>

  <div class="abs media" style="left:100px;top:2895px;width:464px;height:279px;background:linear-gradient(180deg,#c9d3dc 0%,#b7c3ce 90%,#a8785c 90%)" role="img" aria-label="Illustration of a hospital room with a bed and filtration unit"></div>
  <div class="abs card" style="left:585px;top:2924px;width:514px;height:280px;justify-content:flex-start;padding-top:118px">
    <h3 style="margin-bottom:2px">9 Minutes</h3>
    <p>Turns over air in a 15 x 20 room in 9 minutes.</p>
  </div>
</section>

<section>
  <h2 class="abs section-title" style="top:3348px">Get In Touch</h2>
  <div class="abs field" style="left:178px;top:3431px;width:416px">Name</div>
  <div class="abs field" style="left:610px;top:3431px;width:410px">Email</div>
  <div class="abs field" style="left:178px;top:3499px;width:416px">Phone</div>
  <div class="abs field" style="left:610px;top:3499px;width:410px">Subjecet</div>
  <div class="abs field" style="left:178px;top:3571px;width:842px">Address</div>
  <div class="abs field" style="left:178px;top:3644px;width:842px;height:93px">Message</div>
  <div class="abs btn" style="left:524px;top:3763px;width:152px;height:47px">Submit →</div>
</section>

<section>
  <div class="abs band"></div>
  <h2 class="abs" style="left:98px;top:3986px;color:#fff;font-size:40px;line-height:48px;font-weight:600">CoraLinks PDF<br>Quick Info Sheet</h2>
  <p class="abs" style="left:528px;top:3972px;color:#fff;font-size:15px">Quick download for a printable information piece on the CoraLinks system.</p>
  <div class="abs btn" style="left:526px;top:4013px;width:344px;height:47px;background:transparent;border:2px solid #fff">CoraLinks PDF Quick Info Sheet →</div>
</section>

<footer>
  <div class="abs logo" style="left:98px;top:4246px;font-size:38px"><span class="mark" style="width:34px;height:34px"></span>CoraLinks</div>
  <svg class="abs" style="left:146px;top:4326px" width="180" height="36" aria-hidden="true">
    <g fill="#1c1b2e"><circle cx="18" cy="18" r="16"/><circle cx="64" cy="18" r="16"/><circle cx="109" cy="18" r="16"/><circle cx="158" cy="18" r="16"/></g>
  </svg>
  <div class="abs foot-h" style="left:416px;top:4232px">Quick Links</div>
  <div class="abs foot-l" style="left:416px;top:4278px">Home</div>
  <div class="abs foot-l" style="left:416px;top:4314px">How it Works</div>
  <div class="abs foot-l" style="left:416px;top:4350px">Resources</div>
  <div class="abs foot-l" style="left:416px;top:4386px">Contact</div>
  <div class="abs foot-h" style="left:594px;top:4232px">Contact Info</div>
  <div class="abs foot-l" style="left:594px;top:4278px"><span style="color:var(--brand)">✉</span>&nbsp; hello@coralinks.com</div>
  <div class="abs foot-l" style="left:594px;top:4314px"><span style="color:var(--brand)">☎</span>&nbsp; 555-014-2290</div>
  <div class="abs foot-h" style="left:847px;top:4232px">Newsletter</div>
  <div class="abs" style="left:847px;top:4277px;width:253px;height:45px;border:1.5px solid var(--line);font-size:14px;color:#777;padding:13px 10px">Enter email Address</div>
  <div class="abs btn" style="left:847px;top:4338px;width:151px;height:47px">Subscribe →</div>
  <p class="abs" style="left:98px;top:4466px;font-size:13px;color:var(--ink)">© 2022 <span style="color:var(--brand)">Coralinks</span>_All right reserved</p>
</footer>

</body>
</html>
```